Leading inbound Tour Operator Silver Maple Voyage needs an e-mail newsletter design and html template

Introduction
We need a newsletter design for a experienced tour-company based in Los Angeles called Silver Maple Voyage Inc www.silvermaplevoyage.com. We are leading inbound Tour Operator, serving Russian-speaking travelers in North America, and we are in business for over 14 years. We provide travel services to our customers including professional tour guide services on East coast and West Coast, coach bus-tours, private transportation, and much more.

Technical specifications for production design html-template of 2 types e-mail-newsletters in russian language.

Company Name
Silver Maple Voyage Inc http://silvermaplevoyage.com

Goal
To increase the involvement of Target Audience in the interaction with the brand, increase loyalty, increase interest in the services of the company, increasing the number of tour and services orders. This is why we use direct mail as one of major marketing instruments. This e-mail html template should be constructed the way allowing us to change pictures and texts. It means that we need reusable templates.

Target Audience:
• 1st design template - business partners. Agencies and tour operators from Russia (Moscow, St. Petersburg, Yekaterinburg) and other Russian-language countries: Ukraine, Belarus, Bulgaria, Latvia. It is the middle-class audience, mostly female, professionals in tourism sphere
• 2nd design template -direct customers. Travelers from former CIS countries: Ukrainian 2/3, Russian 1/3 part. Men and women, middle age (35 years and older), in managerial positions in big companies, have average or above average income, modern and active lifestyle, love to travel and learn new things.

Object of advertising
Multi-day bus tours of the East and West Coast USA.
Examples of tours advertised in the newsletter:
• Canyon Ribbon Journey VIP – http://silvermaplevoyage.ru/en/tours/wonders-of-the-southwest-vip/
• Canyon Ribbon Journey – http://silvermaplevoyage.ru/en/tours/wonders-of-the-southwest-11-days/
• Coast to Coast Loop – http://silvermaplevoyage.ru/en/tours/all-america/
• East Coast and Canada - http://silvermaplevoyage.ru/en/tours/east-coast-and-canada-11-days/
• Los Angeles Grand-tour - http://silvermaplevoyage.ru/en/tours/los-angeles-grand-tour/
• Tour to Las Vegas - http://silvermaplevoyage.ru/en/tours/las-vegas-2-days/

Description of the advertised tour
Multi-day bus tours for 50 people. Cost is average. The tour price includes: transfers between cities, excursions along the route, DBL hotel accommodation and breakfasts.

This is important
There is a lot of e-mails everyday sent about tourism, our goal is to stand out of the competitors, and to present company’s service clear and understandable, engaging and interesting at the same time.

Corporate Identity
Color: gold (5/29/100/0), red (14/99/100/0) combined with black / white.
Font: Century Gothic Helvetica OR
Company’s Symbol: Star in the logo (image attached).

Our wishes to the e-mail structure
(Please be advised that the order of the blocks is not required. We would like to get vision of the designer – the best way to present information).
• Block 1 - Contact and logo
• Block 2 – Introductory text ( useful information like news update about USA or any other interesting up-to-date fact catching the eye of the audience) and an important message from the president (including pictures and sign)
• Block 3 - Information about the most important tour in this period of time. This unit should be the most important in the layout, emotionally isolated and eye-catching.
• Block 3 – 6 - scheduled tours or excursions. It is important that the information was easily readable and drawing the attention.

Design difference between 2 types of e-mails
• the 1st design template – for business partners. It should has a table structure, to be very simple and readable even if we will show up to 8 type of tours. So the main descriptions of this template is tabular
• the 2nd design template – for direct customers. It should have the unique and interesting element, which will draw clients’ attention so they wish to read our e-mail from the beginning to the end.

Email size
No larger than 600 px. in width and no more than 2 screens.

Design our previous emails
http://mail.pelnorix-archive.com/?u=7a2c91e0f4b3d6a8c5e1f9207&id=c8d1e0a2f3
http://mail.pelnorix-archive.com/?u=7a2c91e0f4b3d6a8c5e1f9207&id=d4a7b9e6c1

• Examples of e-mails that we like PLUS: http://r.quavelto.com/V7P/mv.aspx?k=tRbWkeLpZx2mmQsc8gh3HH41plQdfnuaXkBT7K-3D8FxVyTbNrsLPRQ$$
http://brenwickfund.trelmail.com/t/ViewEmail/j/8A14F7E2B09D35C1/5E9B2C7D41A086F3E2D19B7CA40E6F58

Text for use in e-mail

Contacts
Теl. +1 (800) 555-0148
Skype silver_maple3816
E-mail info@silvermaplevoyage.com

Social networks widgets:
Facebook - https://www.facebook.com/silvermaplevoyage.ru
Vkontakte - http://vk.com/silvermaplevoyage
Instagram - http://instagram.com/silvermaplevoyage
Twitter - https://twitter.com/SilverMapleVoyage
Youtube -https://www.youtube.com/channel/UCq7TM3P2wnhRdX_oKLzWbVa

Introductory text
«Добрый день!

В США прибыла рекордная группа туристов из Китая. Количество путешественников превысело 6 000 человек! Что же привлекает в Америке путешественников со всего мира? Вы можете увидеть и оценить главные достопримечательности Запада Америки на нашем официальном видео-канале на YouTube. Приятного просмотра!

C уважением, Олег Кузьмин
президент компании Silver Maple Voyage Inc.»

Description of main advertise tour
Picture, Name, Dates, Cost, Duration, Itinerary, Link to site «View»

«Каньонное кольцо США

Даты заездов 12.09, 03.10, 31.10
Продолжительность 11 дней
Стоимость на чел. $ 1 495

Программа Санта-Барбара - Сан-Франциско - Йосемити - Лас-Вегас - Долина Смерти - каньон Антилопы - трасса 66 - Гранд Каньон - Сан-Диего - Лос-Анджелес
Узнать подробнее»

Scheduled tours or excursions
Name of this block – РАСПИСАНИЕ ТУРОВ SILVER MAPLE VOYAGE
Description for each tours – Picture, Date, Name, Cost, Duration, Link to site «View»
«08.06
Лос-Анджелес
$ 95 / 6 часов
Подробнее»

```html
<!DOCTYPE html>
<html lang="ru">
<head>
<meta charset="utf-8">
<title>Silver Maple Voyage — расписание туров</title>
<link rel="stylesheet" href="https://fonts.googleapis.com/css2?family=Mulish:wght@400;700;800&family=Arimo:wght@400&display=swap">
<style>
:root{
  --page-bg:#5e5234;
  --accent-yellow:#ffff5a;
  --accent-red:#dc2a2a;
  --panel-dark:#1e1e1e;
  --text-light:#e8e8e8;
  --footer-text:#f2e54c;
  --icon-gold:#d9a520;
  --ink:#111111;
}
*{box-sizing:border-box;margin:0;padding:0}
html,body{width:907px;height:1200px;overflow:hidden}
body{background:var(--page-bg);font-family:"Mulish",sans-serif;position:relative}
.newsletter{position:absolute;left:150px;top:0;width:600px}
.promo-band{height:74px;background:var(--accent-yellow);padding:17px 0 0 36px}
.btn-red{display:inline-block;width:154px;height:33px;background:var(--accent-red);color:#fff;font-weight:700;font-size:13.5px;line-height:33px;text-align:center;text-decoration:none}
.schedule{margin-top:39px;height:788px;background:var(--panel-dark);padding:0 3px}
.schedule-title{height:49px;line-height:50px;text-align:center;color:var(--accent-yellow);font-weight:800;font-size:17px;letter-spacing:.2px}
.tour-grid{display:grid;grid-template-columns:196px 195px 196px;column-gap:3px;row-gap:31px}
.tour-photo{height:215px}
.tour-grid .row-two .tour-photo{height:217px}
.tour-info{padding:11px 0 0 11px;line-height:22px}
.tour-date,.tour-city{color:var(--accent-yellow);font-weight:800;font-size:14px}
.tour-price{color:var(--text-light);font-size:14px}
.btn-yellow{display:block;margin:10px 0 0 10px;width:177px;height:40px;background:var(--accent-yellow);color:var(--ink);font-weight:800;font-size:14px;line-height:40px;text-align:center;text-decoration:none}
.photo-hollywood{background:linear-gradient(160deg,#2a6fd0 0%,#3a86dc 45%,#2d5a2a 85%,#1f3a1c 100%)}
.photo-la{background:linear-gradient(180deg,#f7b35a 0%,#eeb36c 45%,#8a6a3a 75%,#3a3320 100%)}
.photo-bridge{background:linear-gradient(180deg,#1a72d0 0%,#4c98dc 50%,#7a7c80 80%,#55585c 100%)}
.photo-nyc{background:linear-gradient(180deg,#3b8fe0 0%,#a8cdf0 40%,#8a8680 70%,#5a5650 100%)}
.photo-boston{background:linear-gradient(180deg,#1f3fb0 0%,#4a70d0 35%,#d8d8d8 60%,#8a8a90 100%)}
.photo-vegas{background:linear-gradient(180deg,#2c5cb8 0%,#b9cde6 35%,#d8c6a2 60%,#3fb5b0 85%,#2a9a98 100%)}
.site-footer{position:absolute;left:150px;top:934px;width:600px;text-align:center;font-family:"Arimo",sans-serif;color:var(--footer-text);font-size:11.5px}
.social-row{display:flex;justify-content:center;gap:17px;height:24px}
.contact-lines{margin-top:24px;line-height:18px}
.legal{margin-top:15px;line-height:15px}
.legal p:first-child{margin-bottom:3px}
</style>
</head>
<body>
<main class="newsletter">
  <section class="promo-band">
    <a class="btn-red" href="#">Узнать подробнее</a>
  </section>

  <section class="schedule">
    <h2 class="schedule-title">РАСПИСАНИЕ ТУРОВ SILVER MAPLE VOYAGE</h2>
    <div class="tour-grid">
      <article class="tour-card">
        <div class="tour-photo photo-hollywood" role="img" aria-label="Пальма и уличный указатель бульвара в Лос-Анджелесе на фоне неба"></div>
        <div class="tour-info"><p class="tour-date">24.06</p><p class="tour-city">Лос-Анджелес</p><p class="tour-price">$ 95 / 6 часов</p></div>
        <a class="btn-yellow" href="#">Узнать подробнее</a>
      </article>
      <article class="tour-card">
        <div class="tour-photo photo-la" role="img" aria-label="Пальмы и небоскрёбы Лос-Анджелеса на закате"></div>
        <div class="tour-info"><p class="tour-date">27.06, 25.07, 08.08</p><p class="tour-city">Лос-Анджелес</p><p class="tour-price">$ 95 / 6 часов</p></div>
        <a class="btn-yellow" href="#">Узнать подробнее</a>
      </article>
      <article class="tour-card">
        <div class="tour-photo photo-bridge" role="img" aria-label="Красный подвесной мост и автомобили на дороге"></div>
        <div class="tour-info"><p class="tour-date">24.06</p><p class="tour-city">Лос-Анджелес</p><p class="tour-price">$ 95 / 6 часов</p></div>
        <a class="btn-yellow" href="#">Узнать подробнее</a>
      </article>
      <article class="tour-card row-two">
        <div class="tour-photo photo-nyc" role="img" aria-label="Панорама небоскрёбов Нью-Йорка"></div>
        <div class="tour-info"><p class="tour-date">24.06</p><p class="tour-city">Лос-Анджелес</p><p class="tour-price">$ 95 / 6 часов</p></div>
        <a class="btn-yellow" href="#">Узнать подробнее</a>
      </article>
      <article class="tour-card row-two">
        <div class="tour-photo photo-boston" role="img" aria-label="Здание с куполом и колоннами рядом с высотной башней"></div>
        <div class="tour-info"><p class="tour-date">27.06, 25.07, 08.08</p><p class="tour-city">Лос-Анджелес</p><p class="tour-price">$ 95 / 6 часов</p></div>
        <a class="btn-yellow" href="#">Узнать подробнее</a>
      </article>
      <article class="tour-card row-two">
        <div class="tour-photo photo-vegas" role="img" aria-label="Отель у озера в Лас-Вегасе под облачным небом"></div>
        <div class="tour-info"><p class="tour-date">24.06</p><p class="tour-city">Лос-Анджелес</p><p class="tour-price">$ 95 / 6 часов</p></div>
        <a class="btn-yellow" href="#">Узнать подробнее</a>
      </article>
    </div>
  </section>
</main>

<footer class="site-footer">
  <div class="social-row" aria-label="Социальные сети">
    <svg width="24" height="24" viewBox="0 0 24 24" aria-hidden="true"><circle cx="12" cy="12" r="12" fill="var(--icon-gold)"/></svg>
    <svg width="24" height="24" viewBox="0 0 24 24" aria-hidden="true"><circle cx="12" cy="12" r="12" fill="var(--icon-gold)"/></svg>
    <svg width="24" height="24" viewBox="0 0 24 24" aria-hidden="true"><circle cx="12" cy="12" r="12" fill="var(--icon-gold)"/></svg>
  </div>
  <div class="contact-lines">
    <p>Silver Maple Voyage Inc.</p>
    <p>4410 Linden Crest Ave. Suite 318 · Cedar Hollow · CA 90871</p>
    <p>toll free 1.800.555.0148 · office 323.555.0172 · fax 323.555.0195</p>
  </div>
  <div class="legal">
    <p>Copyright © 2014 Silver Maple Voyage Inc., All rights reserved.</p>
    <p>Вы получили данный e-mail, потому что находитесь в нашей базе данных. Если вы больше не хотите<br>получать нашу рассылку, пожалуйста, нажмите отписаться от рассылки.</p>
  </div>
</footer>
</body>
</html>
```